Bold Website Redesign for a Disruptive Training Brand

Corvane Labs is a bold, no-fluff sales & leadership training company powered by AI-driven practice and behavioral science. We’ve already built our website structure and copy in Lovable.ai — now we need a designer to fully transform the visual design across all pages (Home, Approach, Programs, About, Contact).
We’re looking for a modern, memorable, high-performance aesthetic that blends human energy, science, and tech without feeling corporate or safe. Clean, bold typography, fluid layout, strong emotional hero moments, subtle motion, and imagery that mixes real people with abstract scientific/tech visuals.Because our clients are primarily North American, please ensure any human photography or AI-generated imagery reflects a North American business context and demographics (modern, diverse, and realistic).

Your job is visual redesign only — no coding required.
The final design must be practical to rebuild inside Lovable.ai.

A full, detailed creative brief (plus logo files) is included in the uploaded files.
If you can bring a mix of edge, intelligence, and strong visual storytelling, we’d love to see your work.

Website is already built in Lovable.ai at - https://corvane-website-tempdesign.plinkora-sites.app — structure is set, visuals need redesign.

Sick

```html
<!DOCTYPE html>
<html lang="en">
<head>
<meta charset="utf-8">
<title>Corvane Labs — Training that practices back</title>
<link href="https://fonts.googleapis.com/css2?family=Figtree:wght@400;500;600;700&display=swap" rel="stylesheet">
<style>
  :root{
    --navy:#0b1d3f;
    --navy-deep:#081634;
    --blue:#3a62b3;
    --blue-light:#5ec8ea;
    --ink:#0c0f17;
    --muted:#4a5263;
    --pale:#edf1f7;
    --white:#ffffff;
  }
  *{box-sizing:border-box;margin:0;padding:0}
  html,body{width:1200px;height:4700px;overflow:hidden}
  body{font-family:"Figtree",sans-serif;color:var(--ink);background:var(--white);position:relative}
  .abs{position:absolute}

  /* header */
  .site-header{position:absolute;top:0;left:0;width:1200px;height:86px;z-index:5;border-bottom:1px solid rgba(255,255,255,.08)}
  .brand{position:absolute;left:118px;top:30px;color:var(--white);font-weight:700;font-size:15px;letter-spacing:.14em;text-transform:uppercase;display:flex;align-items:center;gap:8px}
  .brand-dot{width:12px;height:12px;border-radius:50%;background:var(--white)}
  .main-nav{position:absolute;left:547px;top:34px;display:flex;gap:0;color:var(--white);font-size:13px}
  .main-nav span{display:inline-flex;align-items:center;gap:5px}
  .nav-home{margin-right:38px}.nav-approach{margin-right:34px}.nav-programs{margin-right:34px}.nav-about{margin-right:31px}
  .nav-cta{position:absolute;left:999px;top:21px;width:95px;height:44px;border:1.5px solid var(--white);border-radius:22px;color:var(--white);font-size:13px;display:flex;align-items:center;justify-content:center}

  /* hero */
  .hero{position:absolute;top:0;left:0;width:1200px;height:833px;
    background:
      radial-gradient(ellipse 60% 22% at 35% 60%, rgba(70,90,220,.55), transparent 70%),
      radial-gradient(ellipse 45% 25% at 80% 66%, rgba(120,60,210,.55), transparent 70%),
      radial-gradient(ellipse 40% 18% at 10% 72%, rgba(40,110,190,.45), transparent 70%),
      linear-gradient(180deg,#0a1a3a 0%,#0c1d45 45%,#141f55 75%,#0d1a44 100%)}
  .hero-title{position:absolute;top:272px;left:0;width:1200px;text-align:center;color:var(--white);font-size:62px;font-weight:500;line-height:66px;letter-spacing:-.01em}
  .hero-lede{position:absolute;top:422px;left:300px;width:600px;text-align:center;color:#e4e8f4;font-size:14px;line-height:21px}
  .hero-actions{position:absolute;top:514px;left:0;width:1200px;display:flex;justify-content:center;gap:14px}
  .btn{height:44px;border-radius:22px;font-size:13px;display:inline-flex;align-items:center;justify-content:center;padding:0 20px;color:var(--white)}
  .btn-solid{background:var(--blue)}
  .btn-ghost{border:1.5px solid var(--white)}

  /* problem */
  .problem{position:absolute;top:833px;left:0;width:1200px;height:810px;background:var(--white)}
  .eyebrow{position:absolute;left:107px;top:109px;color:var(--blue);font-size:10px;letter-spacing:.12em;font-weight:500}
  .problem-title{position:absolute;left:106px;top:136px;font-size:58px;font-weight:500;line-height:66px;letter-spacing:-.01em}
  .problem-lede{position:absolute;left:107px;top:284px;width:920px;font-size:12.5px;line-height:21px;color:var(--ink)}
  .curve-chart{position:absolute;left:100px;top:367px}
  .curve-chart text{font-family:"Figtree",sans-serif}

  /* pillars */
  .pillar{position:absolute;left:0;width:1200px;height:583px}
  .pillar-text,.pillar-media{position:absolute;top:0;width:600px;height:583px}
  .pillar-title{font-size:46px;font-weight:500;line-height:54px}
  .pillar-copy{font-size:13.5px;line-height:22px;margin-top:12px;width:400px}
  .pillar-learn{top:1643px}
  .pillar-certify{top:2226px}
  .pillar-sustain{top:2809px}
  .tone-pale{background:var(--pale)}
  .tone-navy{background:var(--navy);color:var(--white)}
  .media-track{background:linear-gradient(180deg,#7d8590 0%,#5d6670 40%,#a55a45 70%,#b8654d 100%)}
  .media-race{background:linear-gradient(160deg,#8b8e8a 0%,#555a58 45%,#6f716f 70%,#5b6a4a 100%)}
  .media-spire{background:linear-gradient(180deg,#c4d8e6 0%,#a9c4d6 55%,#90adc0 100%)}

  /* team */
  .team{position:absolute;top:3392px;left:0;width:1200px;height:668px;
    background:linear-gradient(180deg,#a7b3c1 0%,#8b9aae 35%,#5d6f8a 62%,#3c4f70 100%)}
  .team-title{position:absolute;left:107px;top:418px;color:var(--white);font-size:45px;font-weight:500;line-height:53px}
  .team-copy{position:absolute;left:676px;top:375px;width:420px;color:var(--white);font-size:13.5px;line-height:21px}
  .team-btn{position:absolute;left:676px;top:508px;height:44px;padding:0 20px}

  /* cta band */
  .cta-band{position:absolute;top:4060px;left:0;width:1200px;height:230px;background:var(--navy-deep)}
  .cta-text{position:absolute;left:107px;top:104px;color:var(--white);font-size:20px;font-weight:500;line-height:26px}
  .cta-btn{position:absolute;left:483px;top:108px;width:163px;height:45px}

  /* footer */
  .site-footer{position:absolute;top:4290px;left:0;width:1200px;height:410px;background:var(--navy-deep);color:var(--white)}
  .footer-brand{position:absolute;left:107px;top:50px;font-weight:700;font-size:15px;letter-spacing:.14em;text-transform:uppercase;display:flex;align-items:center;gap:8px}
  .footer-tag{position:absolute;left:107px;top:114px;width:290px;font-size:12px;line-height:20px;color:#d8deea}
  .social{position:absolute;top:171px;width:35px;height:35px;border:1.5px solid var(--white);border-radius:50%}
  .footer-col{position:absolute;top:44px}
  .footer-col h4{font-size:16px;font-weight:500;margin-bottom:24px}
  .footer-col li{list-style:none;font-size:12px;line-height:18px;color:#d8deea;margin-bottom:15px}
  .footer-rule{position:absolute;left:0;top:340px;width:1200px;height:1px;background:rgba(255,255,255,.12)}
  .legal{position:absolute;top:376px;font-size:11px;color:#d8deea}
</style>
</head>
<body>

<section class="hero" role="img" aria-label="Abstract glowing blue and violet particle wave across a dark navy field">
  <h1 class="hero-title">Training that practices<br>back</h1>
  <p class="hero-lede">AI-driven sustainment that builds mastery — so you don't have to. You'll see measurable growth as your people turn insight into habit — automatically, sustainably, and without extra work for their leaders.</p>
  <div class="hero-actions">
    <span class="btn btn-solid" style="width:152px">See How We Do It</span>
    <span class="btn btn-ghost" style="width:95px">Let's Talk</span>
  </div>
</section>

<header class="site-header">
  <div class="brand"><span class="brand-dot"></span>Corvane Labs</div>
  <nav class="main-nav">
    <span class="nav-home">Home</span>
    <span class="nav-approach">Approach <svg width="9" height="6" viewBox="0 0 9 6"><path d="M1 1l3.5 3.5L8 1" stroke="#fff" fill="none" stroke-width="1.2"/></svg></span>
    <span class="nav-programs">Programs <svg width="9" height="6" viewBox="0 0 9 6"><path d="M1 1l3.5 3.5L8 1" stroke="#fff" fill="none" stroke-width="1.2"/></svg></span>
    <span class="nav-about">About</span>
    <span>Contact</span>
  </nav>
  <span class="nav-cta">Let's Talk</span>
</header>

<section class="problem">
  <p class="eyebrow">PRACTICE MADE PERMANENT</p>
  <h2 class="problem-title">The real problem isn't your people<br>&nbsp;— it's the forgetting curve.</h2>
  <p class="problem-lede">Within a week, most training disappears. Leaders are left guessing who's using what they learned — and no one has time to fix it. We built Corvane Labs to make progress automatic, measurable, and real.</p>

  <svg class="curve-chart" width="1000" height="330" viewBox="0 0 1000 330" aria-label="Forgetting curve chart from Monday to Sunday">
    <text x="23" y="19" font-size="11.5" fill="#1b1f29">Watch how sustained practice changes the curve</text>
    <g font-size="9" fill="#7a8190">
      <text x="22" y="56">100%</text><text x="22" y="104">80%</text><text x="22" y="151">60%</text>
      <text x="22" y="198">40%</text><text x="22" y="246">20%</text><text x="22" y="293">0%</text>
      <text x="65" y="314">Mon</text><text x="215" y="314">Tue</text><text x="366" y="314">Wed</text>
      <text x="520" y="314">Thu</text><text x="670" y="314">Fri</text><text x="821" y="314">Sat</text><text x="958" y="314">Sun</text>
    </g>
    <path d="M65,100 C180,100 250,104 370,136 C450,158 470,180 520,200 C590,228 630,250 675,258 C760,274 870,278 977,280 L977,284 Q977,290 971,290 L71,290 Q65,290 65,284 Z" fill="#3a64b0"/>
    <path d="M65,100 C180,100 250,104 370,136 C450,158 470,180 520,200 C590,228 630,250 675,258 C760,274 870,278 977,280" fill="none" stroke="#5ec8ea" stroke-width="2"/>
    <rect x="368" y="120" width="4" height="172" fill="#fff"/>
    <rect x="673" y="240" width="4" height="52" fill="#fff"/>
    <path d="M65,97 C200,92 330,90 450,94 C560,98 600,104 680,104 C760,104 800,96 860,98 C920,100 950,106 977,108" fill="none" stroke="#5ec8ea" stroke-width="2" stroke-dasharray="6 4"/>
    <text x="80" y="80" font-size="12" fill="#111">People forget fast</text>
    <text x="450" y="145" font-size="12" fill="#111">Within a week 70% is gone</text>
    <text x="821" y="227" font-size="16" fill="#111">We built the fix in.</text>
  </svg>
</section>

<section class="pillar pillar-learn">
  <div class="pillar-text tone-pale" style="left:0">
    <div style="position:absolute;left:107px;top:240px">
      <h3 class="pillar-title">Learn</h3>
      <p class="pillar-copy">Fast, focused workshops, built on science, that install the mindset and skills that matter most.</p>
    </div>
  </div>
  <div class="pillar-media media-track" style="left:600px" role="img" aria-label="Two hurdlers clearing barriers on a red running track before empty stadium seating"></div>
</section>

<section class="pillar pillar-certify">
  <div class="pillar-media media-race" style="left:0" role="img" aria-label="Aerial view of a red race car rounding a barrier-lined street circuit"></div>
  <div class="pillar-text tone-navy" style="left:600px">
    <div style="position:absolute;left:80px;top:248px">
      <h3 class="pillar-title">Certify</h3>
      <p class="pillar-copy">Programmatic AI-driven practice and feedback - mastery without management overhead.</p>
    </div>
  </div>
</section>

<section class="pillar pillar-sustain">
  <div class="pillar-text tone-pale" style="left:0">
    <div style="position:absolute;left:80px;top:246px">
      <h3 class="pillar-title">Sustain</h3>
      <p class="pillar-copy">Light-touch challenges and dashboards that keep skills sharp long after training ends.</p>
    </div>
  </div>
  <div class="pillar-media media-spire" style="left:600px" role="img" aria-label="Sharp silver architectural spire rising into a pale blue sky"></div>
</section>

<section class="team" role="img" aria-label="Group of hikers silhouetted on a misty ridge">
  <h2 class="team-title">Built by people<br>who've led the<br>change themselves.</h2>
  <p class="team-copy">Behind Corvane Labs are leaders who've lived the challenge of making learning last. They've scaled companies, built cultures, and led transformation — and now they've designed the system they always wished existed.</p>
  <span class="btn btn-solid team-btn">Meet the Team</span>
</section>

<section class="cta-band">
  <p class="cta-text">Ready to see what lasting capability<br>looks like?</p>
  <span class="btn btn-solid cta-btn">Start a Conversation</span>
</section>

<footer class="site-footer">
  <div class="footer-brand"><span class="brand-dot"></span>Corvane Labs</div>
  <p class="footer-tag">Making learning that sticks through AI-driven sustainment and behavioral science.</p>
  <span class="social" style="left:107px" aria-label="Social profile"></span>
  <span class="social" style="left:151px" aria-label="Social profile"></span>
  <div class="footer-col" style="left:756px">
    <h4>Quick Links</h4>
    <ul><li>Home</li><li>Approach</li><li>Programs</li><li>About</li><li>Contact</li></ul>
  </div>
  <div class="footer-col" style="left:928px">
    <h4>Get in Touch</h4>
    <ul>
      <li style="font-size:11px">4780 W Meridian Ave Suite 220<br>Tempe, AZ 85282</li>
      <li style="font-size:11px">+1 (555) 014-2290</li>
      <li style="font-size:11px">contact@corvanelabs.com</li>
    </ul>
  </div>
  <div class="footer-rule"></div>
  <p class="legal" style="left:107px">© 2025 Corvane Labs. All rights reserved.</p>
  <p class="legal" style="left:886px">Terms &amp; Conditions</p>
  <p class="legal" style="left:1022px">Privacy Policy</p>
</footer>

</body>
</html>
```